Mens Gym Clothing Website - *Exciting project*

Target Market(s)

Young image conscious males who attend gym regularly

Industry/Entity Type

Clothing

Requirements
Must have
• Large image or multiple images (as belwick) on homepage

```html
<!DOCTYPE html>
<html lang="en">
<head>
<meta charset="utf-8">
<title>Vantor Clothing – Fitness Clothing Superstore</title>
<link rel="stylesheet" href="https://fonts.googleapis.com/css2?family=Arimo:wght@400;700&family=PT+Serif&family=Ubuntu:wght@400;500&family=Kaushan+Script&display=swap">
<style>
:root{
  --page:#f3f3f3;
  --ink:#333;
  --muted:#888;
  --light:#aaa;
  --blue:#2a9fd8;
  --blue-dark:#1f7fb4;
  --orange:#e4745a;
  --tag:#ef6f56;
  --panel:#ffffff;
  --line:#e2e2e2;
  --footer:#f6ecdf;
  --dark:#2a2a2a;
  --badge:#dcd6cc;
  --banner-a:#6a6b4e;
  --banner-b:#2b2c22;
}
*{box-sizing:border-box;margin:0;padding:0}
html,body{width:732px;height:1200px;overflow:hidden}
body{background:var(--page);font-family:Arimo,Arial,sans-serif;color:var(--ink);position:relative;font-size:10px}
.abs{position:absolute}
a{color:inherit;text-decoration:none}

/* header */
.brand{left:18px;top:16px;width:234px;height:36px;background:var(--dark);border-radius:3px;padding:3px 8px}
.brand-name{font-size:17px;font-weight:700;color:#fff;letter-spacing:.5px;line-height:18px}
.brand-tag{font-size:9px;color:#fff;line-height:12px}
.welcome{left:302px;top:18px;font-size:10px}
.welcome a,.account,.cart-link{color:var(--blue)}
.account{left:398px;top:18px;font-size:10px;display:flex;align-items:center;gap:4px}
.cart-link{left:480px;top:15px;font-size:10px;display:flex;align-items:center;gap:4px}
.site-search{left:590px;top:14px;width:126px;height:15px;background:var(--dark);border-radius:8px;color:#ddd;font-size:7px;padding:3px 8px}
.flags{left:572px;top:43px;display:flex;gap:3px}
.flags span{width:10px;height:7px;background:#ccc;display:block}
.flags span:nth-child(1){background:#8a93c4}.flags span:nth-child(2){background:#d7d7e8}.flags span:nth-child(3){background:#e8b36a}
.currency{left:624px;top:42px;color:var(--blue);font-size:8px}
.currency-select{left:663px;top:41px;width:52px;height:10px;background:#fff;border:1px solid #ccc;font-size:7px;color:var(--light);padding-left:3px}

/* nav */
.nav{left:16px;top:60px;width:700px;height:28px;background:linear-gradient(#fbfbfb,#e9e9e9);border-bottom:1px solid #d5d5d5;display:flex;align-items:center;padding-left:6px;gap:6px}
.nav a{font-size:9px;color:var(--muted);padding:4px 6px;border-radius:10px;border:1px solid #e0e0e0}
.nav a.active{background:var(--blue);color:#fff;border-color:var(--blue)}
.nav-search{position:absolute;left:539px;top:4px;width:116px;height:18px;border-radius:9px;background:#f6f6f6;border:1px solid #e2e2e2}
.nav-search-label{position:absolute;right:3px;top:9px;font-size:9px;color:var(--muted);font-weight:700}

/* banner */
.hero{left:16px;top:100px;width:700px;height:228px;background:radial-gradient(ellipse at 60% 40%,var(--banner-a),var(--banner-b));box-shadow:0 6px 8px rgba(0,0,0,.25)}
.hero-offer{left:56px;top:178px;font-family:'Kaushan Script',cursive;font-size:28px;line-height:30px;color:#c84a37}
.hero-sub{left:116px;top:254px;font-size:20px;color:#f1ecd6;font-family:Arimo,sans-serif}
.hero-dots{left:343px;top:296px;display:flex;gap:6px}
.hero-dots span{width:7px;height:7px;border-radius:50%;background:#fff;display:block}
.hero-dots span:first-child{background:#222;border:1px solid #fff}

/* sidebar */
.box{background:var(--panel);border:1px solid var(--line)}
.cart-box{left:16px;top:348px;width:157px;height:102px;padding:16px 12px}
.cart-title{font-family:'PT Serif',serif;font-size:12px}
.cart-empty{color:var(--blue);font-size:8px;margin-top:6px}
.checkout{position:absolute;left:13px;top:62px;width:72px;height:24px;border:1px solid #ccc;font-family:'PT Serif',serif;font-size:10px;display:flex;align-items:center;justify-content:center}
.promo{left:16px;top:464px;width:157px;height:106px}
.promo-top{height:58px;background:var(--orange);padding:10px 14px;color:#fff}
.promo-title{font-family:'PT Serif',serif;font-size:19px;line-height:22px}
.promo-small{font-family:'PT Serif',serif;font-size:9px;letter-spacing:.3px}
.promo-bottom{height:48px;background:#767676;color:#e6e6e6;padding:8px 14px;font-family:'PT Serif',serif;font-style:italic;font-size:9px;line-height:11px}
.products-head{left:16px;top:585px;width:157px;height:28px;display:flex;align-items:center;gap:6px;padding-left:6px;font-family:'PT Serif',serif;font-size:12px}
.cat-list{left:16px;top:613px;width:157px;list-style:none}
.cat-list li{height:35.8px;border:1px solid var(--line);border-top:none;background:var(--panel);display:flex;align-items:center;gap:12px;padding-left:10px;font-size:10px;color:#555}

/* shirt icon */
.shirt{width:12px;height:12px;flex:none}

/* featured */
.section-head{left:187px;top:348px;width:529px;height:27px;border-bottom:2px solid #ddd;padding:7px 16px;font-family:'PT Serif',serif;font-size:12px;font-weight:400;background:linear-gradient(#f7f7f7,#eee)}
.card{width:127px;height:194px;background:var(--panel);border:1px solid #ececec}
.card-photo{position:absolute;left:3px;top:3px;width:120px;height:128px}
.price{position:absolute;left:12px;top:101px;background:var(--tag);color:#fff;font-size:10px;padding:3px 8px;border-radius:2px}
.card-text{position:absolute;left:7px;top:135px;width:116px;font-size:8px;line-height:11px;color:var(--light)}
.add{position:absolute;left:12px;top:167px;width:58px;height:16px;background:#f1f1f1;font-size:10px;display:flex;align-items:center;justify-content:center;gap:4px}

/* info boxes */
.info{width:127px;height:115px;background:var(--panel);border:1px solid #ececec;padding:8px 6px}
.info-title{display:flex;align-items:center;gap:7px;color:var(--blue);font-size:12px;font-weight:700}
.info ul{list-style:none;margin-top:5px;padding-left:11px}
.info li{display:flex;align-items:center;gap:6px;font-size:8px;color:#555;height:21.5px}
.info-more{font-size:7px;color:var(--blue);margin-top:-3px;padding-left:11px}

/* signup */
.signup{left:188px;top:956px;font-family:Ubuntu,sans-serif;color:var(--blue);font-size:12px;white-space:nowrap;line-height:22px}
.signup b{font-weight:500;font-size:18px}
.signup .faint{color:#9bcbe6}
.signup-input{left:515px;top:958px;width:128px;height:18px;border-radius:9px;background:#fbeeee;border:1px solid #ead7d7}
.signup-btn{left:651px;top:957px;width:64px;height:19px;border-radius:9px;background:linear-gradient(#fbd7d7,#f3b3b3);color:#c22;font-size:11px;display:flex;align-items:center;justify-content:center}

/* footer */
.footer{left:16px;top:1037px;width:700px;height:128px;background:var(--footer);box-shadow:0 2px 4px rgba(0,0,0,.12)}
.foot-links{list-style:none;width:108px}
.foot-links li{height:21.6px;border-bottom:1px dashed #ccc;font-size:8px;padding-top:5px}
.partner{left:353px;top:1070px;width:42px;height:46px;background:var(--badge);border-radius:4px}
.cert{background:#dfe2e8;border:1px solid #9aa}
.social{left:525px;font-size:8px;display:flex;align-items:center;gap:8px}
.social i{width:18px;height:18px;border-radius:50%;display:block}
.pay{top:1121px;width:24px;height:17px;border-radius:2px}
.copyright{left:494px;top:1182px;font-size:8px;color:var(--light)}
</style>
</head>
<body>

<header>
  <div class="abs brand">
    <div class="brand-name">VANTOR CLOTHING</div>
    <div class="brand-tag">The No.1 Fitness Clothing Superstore</div>
  </div>
  <div class="abs welcome">Welcome &nbsp;<a href="#">( Log in )</a></div>
  <a class="abs account" href="#">
    <svg width="18" height="16" viewBox="0 0 18 16"><circle cx="9" cy="5" r="4" fill="#c8843a"/><path d="M2 16c0-5 3-6 7-6s7 1 7 6z" fill="#333"/></svg>
    Your account</a>
  <a class="abs cart-link" href="#">
    <svg width="18" height="16" viewBox="0 0 18 16"><path d="M1 2h3l2 9h9l2-7H5" fill="none" stroke="#2a9fd8" stroke-width="2"/><circle cx="7" cy="14" r="1.5" fill="#2a9fd8"/><circle cx="14" cy="14" r="1.5" fill="#2a9fd8"/></svg>
    <span style="color:#333">Cart:</span> (Empty)</a>
  <div class="abs site-search">Search entire store here...</div>
  <div class="abs flags"><span></span><span></span><span></span></div>
  <div class="abs currency">currency</div>
  <div class="abs currency-select">Dollar</div>
</header>

<nav class="abs nav">
  <a class="active" href="#">HOME</a>
  <a href="#">BRANDS</a>
  <a href="#">CLOTHING</a>
  <a href="#">FAQ's</a>
  <a href="#">NEW &amp; STOCK UPDATES</a>
  <span class="nav-search"></span>
  <span class="nav-search-label">SEARCH</span>
</nav>

<section class="abs hero" role="img" aria-label="Photo of a young man in a white graphic T-shirt and sunglasses pointing, against a worn olive wall with floral ornaments"></section>
<div class="abs hero-offer">SUMMER<br>OFFER 60% OFF</div>
<div class="abs hero-sub">ON - LINE SHOP</div>
<div class="abs hero-dots"><span></span><span></span><span></span></div>

<aside>
  <div class="abs box cart-box">
    <div class="cart-title">CART &nbsp;▲</div>
    <div class="cart-empty">No - Products</div>
    <a class="checkout" href="#">CHECK OUT</a>
  </div>
  <div class="abs promo">
    <div class="promo-top"><div class="promo-title">Free Shipping</div><div class="promo-small">ON ORDERS OVER $ 999</div></div>
    <div class="promo-bottom">This offer is valid on all our<br>store items</div>
  </div>
  <div class="abs box products-head">
    <svg width="20" height="18" viewBox="0 0 20 18"><rect x="2" y="6" width="16" height="11" fill="#c8843a"/><rect x="1" y="3" width="18" height="4" fill="#e8b36a"/></svg>
    PRODUCTS
  </div>
  <ul class="abs cat-list">
    <li><svg class="shirt" viewBox="0 0 12 12"><path d="M3 1l-3 3 2 2 1-1v7h6V5l1 1 2-2-3-3H8a2 2 0 0 1-4 0z" fill="#444"/></svg>Brands</li>
    <li><svg class="shirt" viewBox="0 0 12 12"><path d="M3 1l-3 3 2 2 1-1v7h6V5l1 1 2-2-3-3H8a2 2 0 0 1-4 0z" fill="#444"/></svg>T-Shirts</li>
    <li><svg class="shirt" viewBox="0 0 12 12"><path d="M3 1l-3 3 2 2 1-1v7h6V5l1 1 2-2-3-3H8a2 2 0 0 1-4 0z" fill="#444"/></svg>Polo / Knits</li>
    <li><svg class="shirt" viewBox="0 0 12 12"><path d="M3 1l-3 3 2 2 1-1v7h6V5l1 1 2-2-3-3H8a2 2 0 0 1-4 0z" fill="#444"/></svg>Sweatshirts</li>
    <li><svg class="shirt" viewBox="0 0 12 12"><path d="M3 1l-3 3 2 2 1-1v7h6V5l1 1 2-2-3-3H8a2 2 0 0 1-4 0z" fill="#444"/></svg>OuterWear</li>
    <li><svg class="shirt" viewBox="0 0 12 12"><path d="M3 1l-3 3 2 2 1-1v7h6V5l1 1 2-2-3-3H8a2 2 0 0 1-4 0z" fill="#444"/></svg>Woven Shirts</li>
    <li><svg class="shirt" viewBox="0 0 12 12"><path d="M3 1l-3 3 2 2 1-1v7h6V5l1 1 2-2-3-3H8a2 2 0 0 1-4 0z" fill="#444"/></svg>Caps</li>
    <li><svg class="shirt" viewBox="0 0 12 12"><path d="M3 1l-3 3 2 2 1-1v7h6V5l1 1 2-2-3-3H8a2 2 0 0 1-4 0z" fill="#444"/></svg>Ladies</li>
    <li><svg class="shirt" viewBox="0 0 12 12"><path d="M3 1l-3 3 2 2 1-1v7h6V5l1 1 2-2-3-3H8a2 2 0 0 1-4 0z" fill="#444"/></svg>Youth</li>
    <li><svg class="shirt" viewBox="0 0 12 12"><path d="M3 1l-3 3 2 2 1-1v7h6V5l1 1 2-2-3-3H8a2 2 0 0 1-4 0z" fill="#444"/></svg>Infant &amp; Toddler</li>
    <li><svg class="shirt" viewBox="0 0 12 12"><path d="M3 1l-3 3 2 2 1-1v7h6V5l1 1 2-2-3-3H8a2 2 0 0 1-4 0z" fill="#444"/></svg>Tall</li>
  </ul>
</aside>

<main>
  <h2 class="abs section-head">FEATURED ITEMS</h2>

  <div class="abs card" style="left:187px;top:389px"><div class="card-photo" role="img" aria-label="Photo of a couple in red and blue long-sleeve tops" style="background:linear-gradient(135deg,#d8c46a,#c2533e 50%,#3a6fb0)"></div><span class="price">$245.66</span><p class="card-text">It is not like pushing a typical walker. Instead.</p><a class="add" href="#">Add <b>+</b></a></div>
  <div class="abs card" style="left:321px;top:389px"><div class="card-photo" role="img" aria-label="Photo of a navy T-shirt with a snowman print" style="background:linear-gradient(#f0f0f0,#1d2440 40%,#1d2440)"></div><span class="price">$185.66</span><p class="card-text">It is not like pushing a typical walker. Instead.</p><a class="add" href="#">Add <b>+</b></a></div>
  <div class="abs card" style="left:455px;top:389px"><div class="card-photo" role="img" aria-label="Photo of a man in a white graphic T-shirt" style="background:linear-gradient(#7a6a4a,#e0ddd6 60%,#cfc9bf)"></div><span class="price">$345.66</span><p class="card-text">It is not like pushing a typical walker. Instead.</p><a class="add" href="#">Add <b>+</b></a></div>
  <div class="abs card" style="left:589px;top:389px"><div class="card-photo" role="img" aria-label="Photo of a young couple in printed white T-shirts" style="background:linear-gradient(#a8735a,#e6ddd2 60%,#c9a88c)"></div><span class="price">$549.66</span><p class="card-text">It is not like pushing a typical walker. Instead.</p><a class="add" href="#">Add <b>+</b></a></div>

  <div class="abs card" style="left:187px;top:598px"><div class="card-photo" role="img" aria-label="Photo of a woman in an illustrated print T-shirt" style="background:linear-gradient(#d9c4a8,#efe6dc 60%,#7a5a44)"></div><span class="price">$245.66</span><p class="card-text">It is not like pushing a typical walker. Instead.</p><a class="add" href="#">Add <b>+</b></a></div>
  <div class="abs card" style="left:321px;top:598px"><div class="card-photo" role="img" aria-label="Photo of a tan hooded work jacket" style="background:linear-gradient(#f4f4f4,#a57a4e 40%,#8a6138)"></div><span class="price">$185.66</span><p class="card-text">It is not like pushing a typical walker. Instead.</p><a class="add" href="#">Add <b>+</b></a></div>
  <div class="abs card" style="left:455px;top:598px"><div class="card-photo" role="img" aria-label="Photo of a white apron with a pocket on orange" style="background:linear-gradient(90deg,#d86a2a,#f4f4f4 35%,#f4f4f4 65%,#d86a2a)"></div><span class="price">$345.66</span><p class="card-text">It is not like pushing a typical walker. Instead.</p><a class="add" href="#">Add <b>+</b></a></div>
  <div class="abs card" style="left:589px;top:598px"><div class="card-photo" role="img" aria-label="Photo of a woman wearing a black wide-brim hat" style="background:linear-gradient(#6a9a4a,#e9d6c0 60%,#b6a8b8)"></div><span class="price">$549.66</span><p class="card-text">It is not like pushing a typical walker. Instead.</p><a class="add" href="#">Add <b>+</b></a></div>

  <div class="abs info" style="left:187px;top:807px">
    <div class="info-title"><svg width="22" height="20" viewBox="0 0 22 20"><rect x="2" y="8" width="5" height="12" fill="#2a9fd8"/><rect x="8" y="4" width="5" height="16" fill="#e4745a"/><rect x="14" y="10" width="5" height="10" fill="#6ab04c"/></svg>Marketing</div>
    <ul>
      <li><svg class="shirt" viewBox="0 0 12 12"><path d="M3 1l-3 3 2 2 1-1v7h6V5l1 1 2-2-3-3H8a2 2 0 0 1-4 0z" fill="#444"/></svg>Flyer Wizard</li>
      <li><svg class="shirt" viewBox="0 0 12 12"><path d="M3 1l-3 3 2 2 1-1v7h6V5l1 1 2-2-3-3H8a2 2 0 0 1-4 0z" fill="#444"/></svg>Custom Websites</li>
      <li><svg class="shirt" viewBox="0 0 12 12"><path d="M3 1l-3 3 2 2 1-1v7h6V5l1 1 2-2-3-3H8a2 2 0 0 1-4 0z" fill="#444"/></svg>Custom Catalogs</li>
    </ul>
    <div class="info-more">Learn more...</div>
  </div>
  <div class="abs info" style="left:321px;top:807px">
    <div class="info-title"><svg width="22" height="20" viewBox="0 0 22 20"><rect x="1" y="6" width="20" height="13" rx="2" fill="#8a6a4a"/><rect x="7" y="3" width="8" height="4" fill="none" stroke="#5a4430" stroke-width="2"/></svg>Resources</div>
    <ul>
      <li><svg class="shirt" viewBox="0 0 12 12"><path d="M3 1l-3 3 2 2 1-1v7h6V5l1 1 2-2-3-3H8a2 2 0 0 1-4 0z" fill="#444"/></svg>Shipping Cutoff Times</li>
      <li><svg class="shirt" viewBox="0 0 12 12"><path d="M3 1l-3 3 2 2 1-1v7h6V5l1 1 2-2-3-3H8a2 2 0 0 1-4 0z" fill="#444"/></svg>Brands</li>
      <li><svg class="shirt" viewBox="0 0 12 12"><path d="M3 1l-3 3 2 2 1-1v7h6V5l1 1 2-2-3-3H8a2 2 0 0 1-4 0z" fill="#444"/></svg>Locations</li>
    </ul>
    <div class="info-more">Learn more...</div>
  </div>
  <div class="abs info" style="left:455px;top:807px">
    <div class="info-title"><svg width="22" height="20" viewBox="0 0 22 20"><rect x="2" y="3" width="16" height="14" fill="#dde6ee" stroke="#8aa"/><path d="M5 14l10-9" stroke="#2a9fd8" stroke-width="3"/></svg>Sale</div>
    <ul>
      <li><svg class="shirt" viewBox="0 0 12 12"><path d="M3 1l-3 3 2 2 1-1v7h6V5l1 1 2-2-3-3H8a2 2 0 0 1-4 0z" fill="#444"/></svg>Outlet</li>
      <li><svg class="shirt" viewBox="0 0 12 12"><path d="M3 1l-3 3 2 2 1-1v7h6V5l1 1 2-2-3-3H8a2 2 0 0 1-4 0z" fill="#444"/></svg>On Sale Now</li>
      <li><svg class="shirt" viewBox="0 0 12 12"><path d="M3 1l-3 3 2 2 1-1v7h6V5l1 1 2-2-3-3H8a2 2 0 0 1-4 0z" fill="#444"/></svg>Value Basics</li>
    </ul>
    <div class="info-more">Learn more...</div>
  </div>
  <div class="abs info" style="left:589px;top:807px">
    <div class="info-title"><svg width="22" height="20" viewBox="0 0 22 20"><rect x="2" y="8" width="6" height="12" fill="#2a9fd8"/><rect x="8" y="2" width="7" height="18" fill="#6ab04c"/><rect x="15" y="6" width="5" height="14" fill="#1f7fb4"/></svg>Company</div>
    <ul>
      <li><svg class="shirt" viewBox="0 0 12 12"><path d="M3 1l-3 3 2 2 1-1v7h6V5l1 1 2-2-3-3H8a2 2 0 0 1-4 0z" fill="#444"/></svg>Become a Customer</li>
      <li><svg class="shirt" viewBox="0 0 12 12"><path d="M3 1l-3 3 2 2 1-1v7h6V5l1 1 2-2-3-3H8a2 2 0 0 1-4 0z" fill="#444"/></svg>In The News</li>
      <li><svg class="shirt" viewBox="0 0 12 12"><path d="M3 1l-3 3 2 2 1-1v7h6V5l1 1 2-2-3-3H8a2 2 0 0 1-4 0z" fill="#444"/></svg>Social Responsibility</li>
    </ul>
    <div class="info-more">Learn more...</div>
  </div>

  <div class="abs signup">Don't Miss a Deal! <b>Sign up</b> for <b>e-mail</b> <span class="faint">savings</span></div>
  <div class="abs signup-input"></div>
  <a class="abs signup-btn" href="#">Submit</a>
</main>

<footer class="abs footer">
  <ul class="abs foot-links" style="left:36px;top:10px">
    <li>Contact</li><li>Delivery</li><li>Legal Notice</li><li>Terms and conditions</li><li>About us</li>
  </ul>
  <ul class="abs foot-links" style="left:201px;top:10px">
    <li>New products</li><li>Top sellers</li><li>Specials</li><li>Manufacturers</li><li>Suppliers</li>
  </ul>
</footer>
<div class="abs partner" role="img" aria-label="Shipping partner badge"></div>
<div class="abs cert" style="left:416px;top:1052px;width:73px;height:36px" role="img" aria-label="Payment security certificate"></div>
<div class="abs cert" style="left:416px;top:1099px;width:82px;height:37px" role="img" aria-label="Site security certificate"></div>
<div class="abs social" style="top:1060px"><i style="background:#3b5a98"></i>join us on Circlebook</div>
<div class="abs social" style="top:1084px"><i style="background:#3fb6e6"></i>join us on Chirper</div>
<div class="abs pay" style="left:528px;background:#dfe6f3" role="img" aria-label="Accepted card"></div>
<div class="abs pay" style="left:560px;background:#f0d5c4" role="img" aria-label="Accepted card"></div>
<div class="abs pay" style="left:592px;background:#e8eef6" role="img" aria-label="Accepted card"></div>
<div class="abs pay" style="left:623px;background:#2a4a92" role="img" aria-label="Accepted card"></div>
<div class="abs pay" style="left:654px;background:#3a7cc4" role="img" aria-label="Accepted card"></div>
<div class="abs copyright">© 2012 Powered by ... All rights reserved</div>

</body>
</html>
```